Property Development Business Cards

I need a business card design for Tallow Creek Developments Pty Ltd. We are a property development company in Australia and our name defines the five values that we adhere to, being Profitable, Partnerships, Quality Developments, Eco Friendly and Enduring Design.

I have attached the current logo that I use, it is just five yellow circles connected to a single cricle in the middle.

Target Market(s)

Our Target audience is real estate agents, owners of properties, builders and other trades

Industry/Entity Type

Business

Requirements
Must have
• Want to have two sides to the card, one with details and one to just highlight the company

```html
<!DOCTYPE html>
<html lang="en">
<head>
<meta charset="utf-8">
<title>Tallow Creek Developments – Business Card</title>
<link rel="stylesheet" href="https://fonts.googleapis.com/css2?family=PT+Sans:ital,wght@0,400;0,700;1,700&display=swap">
<style>
  :root {
    --page-bg: #d9d9d9;
    --card-white: #ffffff;
    --card-edge: #dcdcdc;
    --brand-blue: #2d86b8;
    --rule-blue: #3a8fc0;
    --accent-yellow: #f6b51c;
    --back-deep: #0d64a0;
    --back-light: #35b2e0;
    --text-light: #ffffff;
    --icon-light: #4fd0fb;
  }
  * { margin: 0; padding: 0; box-sizing: border-box; }
  html, body { width: 1200px; height: 895px; overflow: hidden; }
  body {
    background: var(--page-bg);
    font-family: "PT Sans", Arial, sans-serif;
    position: relative;
  }
  .card {
    position: absolute;
    top: 302px;
    width: 569px;
    height: 342px;
    border-radius: 16px;
    overflow: hidden;
  }
  .card--front {
    left: 18px;
    background: radial-gradient(ellipse 60% 65% at 50% 42%, var(--card-white) 40%, var(--card-edge) 100%);
  }
  .brand-dot {
    position: absolute;
    left: 254px;
    top: 127px;
    width: 60px;
    height: 60px;
    border-radius: 50%;
    background: var(--accent-yellow);
  }
  .company-name {
    position: absolute;
    left: 0;
    right: 0;
    top: 253px;
    text-align: center;
    font-weight: 700;
    font-size: 22px;
    color: var(--brand-blue);
  }
  .company-rule {
    position: absolute;
    left: 170px;
    width: 228px;
    top: 290px;
    height: 2px;
    background: var(--rule-blue);
  }
  .card--back {
    left: 612px;
    background: var(--card-white);
  }
  .back-panel {
    position: absolute;
    left: 0; top: 0; right: 0;
    height: 288px;
    background: radial-gradient(ellipse 55% 70% at 35% 55%, var(--back-light) 0%, var(--back-deep) 100%);
  }
  .back-mark {
    position: absolute;
    left: 89px;
    top: 118px;
    width: 80px;
    text-align: center;
    color: var(--text-light);
    font-weight: 700;
    font-size: 13px;
    line-height: 1.15;
  }
  .back-mark__dot {
    display: block;
    width: 26px;
    height: 26px;
    margin: 0 auto 6px;
    border-radius: 50%;
    background: var(--icon-light);
  }
  .back-divider {
    position: absolute;
    left: 192px;
    top: 69px;
    width: 1px;
    height: 159px;
    background: rgba(255,255,255,0.7);
  }
  .contact {
    position: absolute;
    left: 208px;
    top: 109px;
    color: var(--text-light);
  }
  .contact__name { font-weight: 700; font-size: 22px; line-height: 24px; }
  .contact__phone { font-weight: 700; font-style: italic; font-size: 15px; letter-spacing: 2px; line-height: 18px; }
  .contact__line { font-size: 17px; line-height: 20px; }
  .contact__web { font-size: 15px; line-height: 20px; }
</style>
</head>
<body>
  <section class="card card--front">
    <span class="brand-dot"></span>
    <h1 class="company-name">Tallow Creek Developments Pty Ltd</h1>
    <div class="company-rule"></div>
  </section>

  <section class="card card--back">
    <div class="back-panel">
      <div class="back-mark"><span class="back-mark__dot"></span>Tallow Creek</div>
      <div class="back-divider"></div>
      <div class="contact">
        <p class="contact__name">Dana Whitford</p>
        <p class="contact__phone">0400 555 318</p>
        <p class="contact__line">PO Box 128, Kinross ACT 2990</p>
        <p class="contact__line">Dana@TallowCreekDevelopments.com.au</p>
        <p class="contact__web">www.tallowcreekdevelopments.com.au</p>
      </div>
    </div>
  </section>
</body>
</html>
```